Cosmetic Company with a focus in nontoxic, sustainable and eco conscious beauty.

I am in the final stages of an eyeliner for launch which works with our lash line. Packaging varies but all eco-friendly and some recyclable, some biodegradable. Plastics are extremely limited. Simple ingredients, simple to use, beautifully designed and crafted.
Each purchase we give a portion to Fern Hollow Trust, Verdant Roots Initiative to offset carbon footprint associated with general business.
Gentle Fawn Certified Products
I am looking for package designs for my bamboo eyeliner container boxes which will either be fully biodegradable tubes OR done using stone paper tuck end boxes (yet to decide on which manufacture to go with) and looking for design ideas that could be used on either or slightly revised to work with one or the other. Dimensions to fit an eyeliner tube which measures 17mmx87mm.
My color palate is matte white, blush pink, gold and emerald green. I want it to be earthy but beautiful and elegant. I have attached my logo as well.
Target Market(s)
18-35YO women, beginner to intermediate makeup and skincare knowledge, makeup artists, eco conscious consumers, zero waste consumers.
Industry/Entity Type
Beauty
Font styles to use
Other font styles liked:
- playfair display is one font we use a lot of but doesn't have to be incorporated
Look and feel

```html
<!DOCTYPE html>
<html lang="en">
<head>
<meta charset="utf-8">
<title>Verabelle Eyeliner Packaging</title>
<link rel="stylesheet" href="https://fonts.googleapis.com/css2?family=Playfair+Display:wght@400&display=swap">
<style>
  :root {
    --bg: #ffffff;
    --matte-white: #f3f3f1;
    --gold: #e0bd67;
    --emerald: #1d5a3a;
    --ink-gold: #8c7a1a;
    --edge: #e6e6e3;
  }
  html, body {
    margin: 0;
    padding: 0;
    width: 1200px;
    height: 994px;
    overflow: hidden;
    background: var(--bg);
  }
  .canvas {
    position: relative;
    width: 1200px;
    height: 994px;
    display: flex;
    align-items: center;
    justify-content: center;
    gap: 150px;
  }
  .panel {
    display: block;
    box-shadow: 0 0 0 1px var(--edge);
  }
  .panel--box { width: 250px; height: 900px; }
  .panel--tube { width: 150px; height: 650px; }
  .panel .field-white { fill: var(--matte-white); }
  .panel .field-gold { fill: var(--gold); }
  .panel .field-emerald { fill: var(--emerald); }
  .brand-name {
    font-family: "Playfair Display", serif;
    font-weight: 400;
    fill: var(--ink-gold);
    letter-spacing: 0.06em;
  }
</style>
</head>
<body>
<main class="canvas">

  <svg class="panel panel--box" viewBox="0 0 100 360" aria-label="Verabelle eyeliner box front">
    <rect class="field-white" x="0" y="0" width="100" height="360"/>
    <polygon class="field-gold" points="0,0 100,0 100,20 0,100"/>
    <polygon class="field-emerald" points="66,0 100,0 100,34"/>
    <polygon class="field-gold" points="0,340 100,260 100,360 0,360"/>
    <polygon class="field-emerald" points="0,318 0,360 40,360"/>
    <text class="brand-name" x="0" y="0" text-anchor="middle" dominant-baseline="central"
          font-size="14" transform="translate(50 180) rotate(-90)">VERABELLE</text>
  </svg>

  <svg class="panel panel--tube" viewBox="0 0 60 260" aria-label="Verabelle eyeliner tube label">
    <rect class="field-white" x="0" y="0" width="60" height="260"/>
    <polygon class="field-gold" points="0,0 60,0 60,14 0,66"/>
    <polygon class="field-emerald" points="40,0 60,0 60,22"/>
    <polygon class="field-gold" points="0,246 60,194 60,260 0,260"/>
    <polygon class="field-emerald" points="0,228 0,260 26,260"/>
    <text class="brand-name" x="0" y="0" text-anchor="middle" dominant-baseline="central"
          font-size="9" transform="translate(30 130) rotate(-90)">VERABELLE</text>
  </svg>

</main>
</body>
</html>
```